The Fernbrook Laundromat - Pre-Opening Marketing Postcard

We need a design for a 6"x11" postcard that we will use to advertise the upcoming opening of a new laundromat in Baldwin, NY. The name of the store is "The Fernbrook Laundromat", and the most important things are: match the colors on the card to our logo colors, but also add in some yellow and possibly red accents; say "Free Dryers" in a big, obvious way; include generic washer/dryer pictures, put a basic map of the location on the back of the card, and leave the right 1/3 of the card blank except for the retail indicia and the name "Local Postal Customer". Please refer to the uploaded file showing an example basic layout for the card.
Target Market(s)
low-to-middle-income residents within a 3-mile radius
Industry/Entity Type
Retail
Requirements
Must have
- - The words FREE DRYERS!
- - A simple, hand-drawn map of the location (412 Ashgrove Road, Baldwin, NY) and major roads nearby (dorset avenue, ashgrove road, elm ave, etc.)
- - The words Opening Soon! (or Opening in March!)
- - The words Newly-Built Laundromat, or New Store!, or something similar
- - The words Local Postal Customer on the back, as shown in my example design layout
- - The retail indicia positioned as shown in my example design layout
- - nothing else on the rear, right-hand 1/3 of the card other than local postal customer and the indicia
Nice to have
- - A transparent background using the generic washers and/or generic dryers pictures
- - Some yellow and red accents or colors to appeal to our hispanic customers
- - The words Professional Wash & Fold Service
Should not have
- - Anything on the back, right-hand 1/3 of the card other than Local Postal Customer and the retail indicia picture

```html
<!DOCTYPE html>
<html lang="en">
<head>
<meta charset="utf-8">
<title>The Fernbrook Laundromat – Pre-Opening Postcard</title>
<link href="https://fonts.googleapis.com/css2?family=Montserrat:wght@500;600;700;800&display=swap" rel="stylesheet">
<style>
  :root {
    --stage: #444444;
    --navy: #0b2f63;
    --blue: #1d4f8f;
    --blue-deep: #123d78;
    --logo-blue: #084a94;
    --pale-teal: #b9d4d0;
    --yellow: #f5e900;
    --red: #c8102e;
    --white: #ffffff;
    --ink: #1a1a1a;
    --bubble: #e4f1f3;
  }
  * { box-sizing: border-box; margin: 0; padding: 0; }
  html, body { width: 1200px; height: 1200px; overflow: hidden; background: var(--stage); }
  body { position: relative; font-family: "Montserrat", Arial, sans-serif; }

  .card {
    position: absolute; left: 155px; width: 927px; height: 504px; overflow: hidden;
  }
  .card--front { top: 78px; }
  .card--back { top: 638px; background: var(--white); }

  .photo-fill {
    position: absolute; top: 0; left: 0; height: 100%;
    background: linear-gradient(160deg, #2a5d9a 0%, var(--blue) 40%, var(--blue-deep) 75%, var(--navy) 100%);
  }
  .card--front .photo-fill { width: 100%; }
  .card--back .photo-fill { width: 503px; }

  .bubble {
    position: absolute; border-radius: 50%;
    background: radial-gradient(circle at 35% 30%, var(--white) 0 18%, var(--bubble) 40%, #b8d2da 100%);
    border: 2px solid var(--logo-blue);
  }

  /* Front */
  .brand-badge {
    position: absolute; left: 51px; top: 140px; width: 280px; height: 280px;
    border-radius: 50%; background: var(--pale-teal);
    display: flex; align-items: center; justify-content: center; text-align: center;
  }
  .brand-badge__name {
    font-weight: 800; font-size: 36px; line-height: 1.08; color: var(--logo-blue);
  }
  .headline {
    position: absolute; left: 432px; font-weight: 800; line-height: 1; white-space: nowrap;
  }
  .headline--free { top: 125px; font-size: 106px; letter-spacing: -1px; color: var(--yellow); }
  .headline--dryers { top: 239px; font-size: 94px; letter-spacing: -2px; color: var(--white); }
  .opening {
    position: absolute; left: 428px; top: 370px; font-weight: 700; font-size: 55px;
    color: var(--white); line-height: 1; white-space: nowrap;
  }
  .ribbon {
    position: absolute; right: -52px; top: 34px; width: 260px; height: 38px;
    background: var(--red); transform: rotate(33deg);
    color: var(--white); font-weight: 700; font-size: 24px; line-height: 38px; text-align: center;
  }

  /* Back */
  .service-title {
    position: absolute; left: 27px; top: 40px; font-weight: 700; font-size: 34px; line-height: 44px;
  }
  .service-title__lead { color: var(--yellow); display: block; }
  .service-title__rest { color: var(--white); display: block; }
  .service-copy {
    position: absolute; left: 31px; top: 148px; width: 205px;
    color: var(--white); font-weight: 700; font-size: 14px; line-height: 17px;
  }
  .service-copy p + p { margin-top: 17px; }
  .map-frame {
    position: absolute; left: 241px; top: 120px; width: 364px; height: 364px;
    border-radius: 50%; background: var(--pale-teal); padding: 14px;
  }
  .map-fill {
    width: 100%; height: 100%; border-radius: 50%;
    background: radial-gradient(circle at 45% 50%, #e2e2e2 0%, #d6d6d6 100%);
  }
  .postal-recipient {
    position: absolute; left: 822px; top: 34px; width: 190px;
    transform: rotate(90deg); transform-origin: 0 0;
    font-weight: 500; font-size: 16px; color: var(--ink); white-space: nowrap;
  }
  .indicia {
    position: absolute; left: 837px; top: 390px; width: 64px; height: 84px;
    border: 1px solid #666;
  }
  .indicia__text {
    position: absolute; left: 62px; top: 2px; width: 80px;
    transform: rotate(90deg); transform-origin: 0 0;
    font-family: Arial, Helvetica, sans-serif; font-weight: 700; font-size: 8.5px; line-height: 10.5px;
    text-align: center; color: var(--ink);
  }
</style>
</head>
<body>

<section class="card card--front" aria-label="Postcard front">
  <div class="photo-fill" role="img" aria-label="Blue-toned photo of a row of front-loading laundromat washers and dryers"></div>

  <span class="bubble" style="left:312px;top:121px;width:44px;height:44px"></span>
  <span class="bubble" style="left:308px;top:172px;width:16px;height:16px"></span>
  <span class="bubble" style="left:342px;top:166px;width:28px;height:28px"></span>
  <span class="bubble" style="left:345px;top:200px;width:20px;height:20px"></span>
  <span class="bubble" style="left:328px;top:222px;width:20px;height:20px"></span>
  <span class="bubble" style="left:744px;top:62px;width:46px;height:46px"></span>
  <span class="bubble" style="left:800px;top:116px;width:16px;height:16px"></span>
  <span class="bubble" style="left:750px;top:210px;width:16px;height:16px"></span>
  <span class="bubble" style="left:368px;top:442px;width:40px;height:40px"></span>

  <div class="brand-badge">
    <p class="brand-badge__name">The<br>Fernbrook<br>Laundromat</p>
  </div>

  <p class="headline headline--free">FREE</p>
  <p class="headline headline--dryers">DRYERS!</p>
  <p class="opening">Opening Soon!</p>

  <div class="ribbon">New Store!</div>
</section>

<section class="card card--back" aria-label="Postcard back">
  <div class="photo-fill" role="img" aria-label="Blue-toned photo of laundromat washers in a row"></div>

  <h2 class="service-title">
    <span class="service-title__lead">Professional Wash</span>
    <span class="service-title__rest">&amp; Fold Service</span>
  </h2>

  <div class="service-copy">
    <p>The Fernbrook Laundromat is a full service laundry center providing laundry services to residential and commercial customers.</p>
    <p>A clean and convenient location, modern equipment and customer&#8209;friendly services are among the many positive features .</p>
  </div>

  <div class="map-frame">
    <div class="map-fill" role="img" aria-label="Simple street map marking 412 Ashgrove Road, with Ashgrove Road, Dorset Ave and nearby avenues"></div>
  </div>

  <span class="bubble" style="left:407px;top:57px;width:34px;height:34px"></span>
  <span class="bubble" style="left:529px;top:70px;width:22px;height:22px"></span>
  <span class="bubble" style="left:534px;top:96px;width:48px;height:48px"></span>
  <span class="bubble" style="left:234px;top:430px;width:36px;height:36px"></span>
  <span class="bubble" style="left:296px;top:456px;width:20px;height:20px"></span>
  <span class="bubble" style="left:542px;top:454px;width:20px;height:20px"></span>

  <p class="postal-recipient">Local Postal Customer</p>

  <div class="indicia">
    <p class="indicia__text">PRSRT STD<br>ECRWSS<br>U.S. POSTAGE<br>PAID<br>EDDM-Retail</p>
  </div>
</section>

</body>
</html>
```